Established food business needs a new name card design

Refer to attached current name card. Would like a new professional look design with only the company name and logo without any pictures. Would like green and yellow to be included.
To include:
My name "IBRAHIM SUKRI" and hand phone number "87260413".
To delete "
"Along Brackendale Ave 8" and
"www.nur-tiwas.com.sg"
To change email to:
"tkr27@velmorix.com.sg"

```html
<!DOCTYPE html>
<html lang="en">
<head>
<meta charset="utf-8">
<title>NUR-TIWAS name card</title>
<link rel="stylesheet" href="https://fonts.googleapis.com/css2?family=Lato:wght@400;700;900&display=swap">
<style>
  :root {
    --stage: #3b3b3b;
    --green-light: #0b5d37;
    --green-deep: #033620;
    --gold: #f1d600;
    --gold-band: #c8b000;
    --gold-band-hi: #efe05a;
    --ink-light: #e8efe9;
  }
  * { box-sizing: border-box; margin: 0; padding: 0; }
  html, body { width: 1200px; height: 866px; overflow: hidden; }
  body {
    background: var(--stage);
    font-family: "Lato", sans-serif;
    display: flex;
    align-items: center;
    justify-content: center;
    gap: 40px;
  }
  .card {
    position: relative;
    width: 540px;
    height: 324px;
    background: radial-gradient(ellipse at 40% 30%, var(--green-light) 0%, var(--green-deep) 85%);
    box-shadow: 0 10px 24px rgba(0,0,0,.45);
    overflow: hidden;
  }
  .card__band {
    position: absolute; left: 0; right: 0; bottom: 0; height: 12px;
    background: linear-gradient(90deg, var(--gold-band), var(--gold-band-hi) 45%, var(--gold-band) 70%, var(--gold-band-hi));
  }
  .brand {
    position: absolute;
    display: flex; align-items: center; gap: 12px;
  }
  .brand__mark { flex: none; }
  .brand__name {
    font-weight: 900; color: var(--gold);
    letter-spacing: 1px; white-space: nowrap;
  }
  .card--front .brand { left: 50%; top: 50%; transform: translate(-50%, -58%); }
  .card--front .brand__name { font-size: 46px; }
  .card--front .brand__rule {
    position: absolute; left: 150px; right: 40px; top: 196px;
    height: 1px; background: var(--gold); opacity: .55;
  }
  .card--back .brand { left: 250px; top: 88px; }
  .card--back .brand__name { font-size: 36px; }
  .card--back .divider {
    position: absolute; left: 60px; right: 40px; top: 150px;
    height: 1px; background: var(--gold); opacity: .5;
  }
  .person { position: absolute; left: 34px; top: 30px; }
  .person__name { font-size: 22px; font-weight: 900; color: var(--gold); letter-spacing: 1px; }
  .person__cell { font-size: 15px; color: var(--gold); margin-top: 2px; }
  .contact { list-style: none; margin-top: 10px; }
  .contact li {
    display: flex; align-items: center; gap: 5px;
    font-size: 14px; color: var(--ink-light); line-height: 1.45;
  }
  .address {
    position: absolute; right: 40px; top: 182px;
    font-size: 15px; line-height: 1.35; color: var(--ink-light);
    font-style: normal; letter-spacing: .5px;
  }
</style>
</head>
<body>

  <section class="card card--front" aria-label="Card front">
    <div class="brand">
      <svg class="brand__mark" width="48" height="48" viewBox="0 0 48 48" aria-hidden="true">
        <circle cx="24" cy="24" r="20" fill="none" stroke="var(--gold)" stroke-width="4"/>
      </svg>
      <span class="brand__name">NUR-TIWAS</span>
    </div>
    <div class="brand__rule"></div>
    <div class="card__band"></div>
  </section>

  <section class="card card--back" aria-label="Card back">
    <div class="person">
      <p class="person__name">IBRAHIM SUKRI</p>
      <p class="person__cell">Cell : 87260413</p>
      <ul class="contact">
        <li>
          <svg width="13" height="11" viewBox="0 0 13 11" aria-hidden="true">
            <path d="M1 3 Q6.5 -1 12 3 L10 5 L8 3.5 L5 3.5 L3 5 Z" fill="var(--gold)"/>
            <rect x="2.5" y="5.5" width="8" height="5" rx="1" fill="var(--gold)"/>
          </svg>64028315
        </li>
        <li>
          <svg width="13" height="10" viewBox="0 0 13 10" aria-hidden="true">
            <rect x=".5" y=".5" width="12" height="9" fill="var(--gold)"/>
            <path d="M.5 .5 L6.5 5.5 L12.5 .5" fill="none" stroke="var(--green-deep)" stroke-width="1"/>
          </svg>tkr27@velmorix.com.sg
        </li>
      </ul>
    </div>
    <div class="brand">
      <svg class="brand__mark" width="40" height="40" viewBox="0 0 40 40" aria-hidden="true">
        <circle cx="20" cy="20" r="16" fill="none" stroke="var(--gold)" stroke-width="3.5"/>
      </svg>
      <span class="brand__name">NUR-TIWAS</span>
    </div>
    <div class="divider"></div>
    <address class="address">
      18 Kelvara Industrial<br>
      Estate Road 2# 02-07<br>
      Singapore 738104
    </address>
    <div class="card__band"></div>
  </section>

</body>
</html>
```